Business Card cabinets and cabinets components making company.

the card should be formal and interesting at the same time. The main colors will be black and white.

Font styles to use
Sans Serif

Colors

Designer to choose only greyscale colors for use in the design.

Requirements
Must have
• At least must have the followings:
office phone
cell phone
address
position
name
email
web

```html
<!DOCTYPE html>
<html lang="en">
<head>
<meta charset="utf-8">
<title>Trimwell Business Card</title>
<link rel="stylesheet" href="https://fonts.googleapis.com/css2?family=Roboto:wght@400;500;700&display=swap">
<style>
  :root {
    --backdrop: #1d1d1f;
    --card-black: #161616;
    --card-white: #ffffff;
    --ink: #111111;
    --ink-soft: #3a3a3a;
    --gloss: #8c8c8c;
    --url: #e8e8e8;
    --rule: #1a1a1a;
  }
  * { box-sizing: border-box; margin: 0; padding: 0; }
  html, body {
    width: 1200px;
    height: 800px;
    overflow: hidden;
    background: var(--backdrop);
    font-family: "Roboto", Arial, sans-serif;
  }
  .stage {
    width: 1200px;
    height: 800px;
    display: flex;
    align-items: center;
    justify-content: center;
    gap: 40px;
  }
  .card {
    position: relative;
    width: 540px;
    height: 309px;
    box-shadow: 0 18px 40px rgba(0,0,0,0.55);
  }

  /* Front: black */
  .card--front {
    background: var(--card-black);
    display: flex;
    flex-direction: column;
    align-items: center;
    justify-content: center;
  }
  .card--front .brand {
    color: var(--gloss);
  }
  .card--front .brand-mark {
    background: var(--gloss);
  }
  .front-rule {
    width: 300px;
    height: 1px;
    background: #4a4a4a;
    margin-top: 10px;
  }
  .web {
    margin-top: 22px;
    color: var(--url);
    font-size: 12px;
    letter-spacing: 5px;
  }

  /* Shared wordmark */
  .brand {
    display: flex;
    align-items: center;
    gap: 12px;
    font-weight: 700;
    font-size: 58px;
    line-height: 1;
    letter-spacing: -1px;
  }
  .brand-mark {
    width: 26px;
    height: 26px;
  }

  /* Back: white */
  .card--back {
    background: var(--card-white);
    color: var(--ink);
  }
  .card--back .brand {
    position: absolute;
    top: 40px;
    right: 38px;
    color: var(--ink);
  }
  .card--back .brand-mark {
    background: var(--ink);
  }
  .brand-rule {
    position: absolute;
    top: 116px;
    right: 28px;
    width: 290px;
    height: 1.5px;
    background: var(--rule);
  }
  .person {
    position: absolute;
    left: 34px;
    top: 178px;
  }
  .person-name {
    font-weight: 700;
    font-size: 19px;
    letter-spacing: 0.3px;
  }
  .person-role {
    font-size: 13px;
    color: var(--ink-soft);
    margin-top: 2px;
  }
  .contact-rule {
    position: absolute;
    left: 34px;
    right: 28px;
    top: 232px;
    height: 1px;
    background: var(--rule);
  }
  .contact {
    position: absolute;
    left: 34px;
    top: 242px;
    font-size: 12.5px;
    line-height: 1;
  }
  .contact-row {
    display: flex;
    align-items: center;
    gap: 8px;
    margin-bottom: 9px;
  }
  .contact-item {
    display: flex;
    align-items: center;
    gap: 5px;
  }
  .sep {
    width: 1px;
    height: 14px;
    background: var(--ink);
  }
  .icon {
    width: 15px;
    height: 15px;
    flex: none;
  }
</style>
</head>
<body>
<main class="stage">

  <section class="card card--front" aria-label="Card front">
    <div class="brand">
      <span class="brand-mark" aria-hidden="true"></span>
      <span class="brand-name">Trimwell</span>
    </div>
    <div class="front-rule"></div>
    <p class="web">www.trimwellcabinets.com</p>
  </section>

  <section class="card card--back" aria-label="Card back">
    <div class="brand">
      <span class="brand-mark" aria-hidden="true"></span>
      <span class="brand-name">Trimwell</span>
    </div>
    <div class="brand-rule"></div>

    <div class="person">
      <p class="person-name">OWEN HARTLEY</p>
      <p class="person-role">Manager</p>
    </div>
    <div class="contact-rule"></div>

    <div class="contact">
      <div class="contact-row">
        <span class="contact-item">
          <svg class="icon" viewBox="0 0 16 16" aria-label="Mobile">
            <circle cx="8" cy="8" r="7.2" fill="none" stroke="#111" stroke-width="1.2"/>
            <rect x="5.6" y="3.8" width="4.8" height="8.4" rx="0.8" fill="none" stroke="#111" stroke-width="1.1"/>
            <line x1="7.3" y1="10.8" x2="8.7" y2="10.8" stroke="#111" stroke-width="1"/>
          </svg>
          555 014 2387
        </span>
        <span class="sep"></span>
        <span class="contact-item">
          <svg class="icon" viewBox="0 0 16 16" aria-label="Office phone">
            <circle cx="8" cy="8" r="7.2" fill="none" stroke="#111" stroke-width="1.2"/>
            <path d="M4.2 7 Q8 3.6 11.8 7 L10.8 8 L9.4 7.2 L6.6 7.2 L5.2 8 Z" fill="#111"/>
            <rect x="5.4" y="8.4" width="5.2" height="3.2" rx="0.6" fill="#111"/>
          </svg>
          555 014 9021
        </span>
        <span class="sep"></span>
        <span class="contact-item">
          <svg class="icon" viewBox="0 0 16 16" aria-label="Email">
            <circle cx="8" cy="8" r="7.2" fill="none" stroke="#111" stroke-width="1.2"/>
            <rect x="4.2" y="5.2" width="7.6" height="5.6" rx="0.5" fill="#111"/>
            <polyline points="4.4,5.6 8,8.4 11.6,5.6" fill="none" stroke="#fff" stroke-width="0.9"/>
          </svg>
          info@trimwellcabinets.com
        </span>
      </div>
      <div class="contact-row">
        <span class="contact-item">
          <svg class="icon" viewBox="0 0 16 16" aria-label="Address">
            <circle cx="8" cy="8" r="7.2" fill="none" stroke="#111" stroke-width="1.2"/>
            <path d="M8 12.4 C6 9.8 5 8.4 5 6.8 A3 3 0 0 1 11 6.8 C11 8.4 10 9.8 8 12.4 Z" fill="none" stroke="#111" stroke-width="1.1"/>
            <circle cx="8" cy="6.8" r="1.1" fill="#111"/>
          </svg>
          PO Box 418, 27 Carden Street, Ballarat
        </span>
      </div>
    </div>
  </section>

</main>
</body>
</html>
```